Business card design needed

It's a new business in town.Something so the name stands out.I need a logo for the B.R.W
I may all so use the design as a sign on a building

Contact Information for Business Card

B.R.W
Brindlewood Auto Detailing
42 Fenwarra Crs
Brindlewood Vic 3799
Ph:(03)59284736
Mob:0417362958

```html
<!DOCTYPE html>
<html lang="en">
<head>
<meta charset="utf-8">
<title>Brindlewood Auto Detailing – Business Card</title>
<link href="https://fonts.googleapis.com/css2?family=Cardo:wght@400;700&display=swap" rel="stylesheet">
<style>
  :root {
    --bg-deep: #1b2b3a;
    --bg-mid: #2a3c4d;
    --bg-light: #45596a;
    --ink-mark: #a9cfd9;
    --ink-strong: #e3e9ee;
    --ink-soft: #bccad5;
    --divider: #0e1b26;
    --car-light: #d9d2c8;
    --car-mid: #a79c8f;
    --car-dark: #2a2622;
  }
  html, body {
    margin: 0;
    padding: 0;
    width: 1200px;
    height: 693px;
    overflow: hidden;
  }
  .card {
    position: relative;
    width: 1200px;
    height: 693px;
    background:
      radial-gradient(ellipse 900px 620px at 1180px 0px, var(--bg-light) 0%, var(--bg-mid) 45%, rgba(42,60,77,0) 100%),
      linear-gradient(180deg, var(--bg-mid) 0%, var(--bg-deep) 100%);
    font-family: "Cardo", Georgia, serif;
  }
  .vehicle-photo {
    position: absolute;
    left: 186px;
    top: 282px;
    width: 268px;
    height: 118px;
    border-radius: 40px 60px 22px 22px;
    background: linear-gradient(160deg, var(--car-light) 0%, var(--car-mid) 60%, var(--car-dark) 100%);
    box-shadow: 0 28px 30px -12px rgba(0, 0, 0, 0.55);
  }
  .divider {
    position: absolute;
    left: 599px;
    top: 172px;
    width: 1px;
    height: 350px;
    background: var(--divider);
  }
  .brand {
    position: absolute;
    left: 600px;
    width: 504px;
    top: 256px;
    text-align: center;
  }
  .brand-mark {
    margin: 0;
    font-weight: 700;
    font-size: 38px;
    line-height: 44px;
    letter-spacing: 3px;
    color: var(--ink-mark);
  }
  .brand-name {
    margin: 5px 0 0;
    font-weight: 700;
    font-size: 25px;
    line-height: 32px;
    color: var(--ink-strong);
  }
  .contact {
    position: absolute;
    left: 759px;
    top: 344px;
    margin: 0;
    font-style: normal;
    font-size: 20px;
    line-height: 24.5px;
    color: var(--ink-soft);
  }
  .contact span { display: block; }
</style>
</head>
<body>
  <div class="card">
    <div class="vehicle-photo" role="img" aria-label="Photo of a white crossover SUV, front three-quarter view"></div>
    <div class="divider"></div>
    <div class="brand">
      <p class="brand-mark">B.R.W</p>
      <h1 class="brand-name">Brindlewood Auto Detailing</h1>
    </div>
    <address class="contact">
      <span>42 Fenwarra Crs</span>
      <span>Brindlewood Vic 3799</span>
      <span>Ph:(03)59284736</span>
      <span>Mob:0417362958</span>
    </address>
  </div>
</body>
</html>
```